Verdant Pathworks Business Card

want the back of card to be blue- with the logo in the center
front of card- info plus logo (info being mailing address, email address, and website address )
4 different names with titles to have on cards
1) Dominic Ashvale - Owner
2) Bethany Korvuth- Customer Relationship Specialist
3) Luca Brennwick- Vice President of Sales
4) Neil Umbright- Chief Technology Officer

Target Market(s)

tech company in the government/probation office industry

Industry/Entity Type

Government Office

Contact Information for Business Card

1) Dominic Ashvale - Owner

Colors
0355a3
ffffff

Requirements
Must have
• back side should be blue, with the logo placed in the center
• front side needs to include both the logo, as well as company info (info should include website address, email address, and mailing address)

```html
<!DOCTYPE html>
<html lang="en">
<head>
<meta charset="utf-8">
<title>Verdant Pathworks Business Card</title>
<link href="https://fonts.googleapis.com/css2?family=Open+Sans:wght@400;700;800&family=Titillium+Web:wght@400;600&display=swap" rel="stylesheet">
<style>
  :root {
    --navy: #1f3366;
    --navy-deep: #182a57;
    --navy-soft: #2b417a;
    --white: #ffffff;
    --paper: #f7f7f7;
    --grey: #7b7b7b;
    --ink: #4a4a4a;
    --backdrop: #2b2b2b;
  }
  * { margin: 0; padding: 0; box-sizing: border-box; }
  html, body {
    width: 1200px; height: 900px; overflow: hidden;
    background: var(--backdrop);
  }
  .stage {
    position: relative; width: 1200px; height: 900px;
    display: flex; flex-direction: column; align-items: center; justify-content: center; gap: 40px;
  }
  .card {
    position: relative; width: 680px; height: 388px; overflow: hidden;
  }
  /* Back side */
  .card-back { background: var(--navy); }
  .back-pattern {
    position: absolute; inset: 0;
    background: linear-gradient(120deg, var(--navy-deep) 0%, var(--navy) 50%, var(--navy-soft) 100%);
  }
  .back-brand {
    position: absolute; left: 0; right: 0; top: 50%; transform: translateY(-50%);
    display: flex; align-items: center; justify-content: center; gap: 14px;
    font-family: "Open Sans", sans-serif; font-weight: 700; font-size: 30px;
    color: var(--white); letter-spacing: 1px;
  }
  .brand-mark { width: 22px; height: 22px; border-radius: 50%; background: var(--white); }
  /* Front side */
  .card-front { background: linear-gradient(135deg, var(--white) 0%, var(--paper) 100%); }
  .front-brand {
    position: absolute; left: 0; right: 0; top: 70px;
    display: flex; flex-direction: column; align-items: center; gap: 16px;
  }
  .front-brand .brand-mark { width: 44px; height: 44px; border-radius: 50%; background: var(--navy); }
  .front-brand .brand-name {
    font-family: "Open Sans", sans-serif; font-weight: 700; font-size: 40px;
    color: var(--navy); letter-spacing: 1px; text-transform: uppercase;
  }
  .person {
    position: absolute; right: 358px; top: 226px; text-align: right;
  }
  .person-name {
    font-family: "Open Sans", sans-serif; font-weight: 800; font-size: 22px;
    color: var(--navy); text-transform: uppercase; letter-spacing: 0.5px;
  }
  .person-title {
    font-family: "Titillium Web", sans-serif; font-size: 16px; color: var(--grey); margin-top: 2px;
  }
  .divider {
    position: absolute; left: 340px; top: 220px; width: 2px; height: 76px; background: var(--grey);
  }
  .contact {
    position: absolute; left: 362px; top: 222px; list-style: none;
    font-family: "Titillium Web", sans-serif; font-size: 17px; color: var(--ink);
  }
  .contact li { display: flex; align-items: center; gap: 10px; height: 24px; }
  .contact svg { width: 16px; height: 16px; fill: var(--navy); flex: none; }
  .address-band {
    position: absolute; left: 0; right: 0; top: 306px; height: 52px;
    background: var(--navy);
    display: flex; align-items: center; justify-content: center;
    font-family: "Titillium Web", sans-serif; font-size: 19px; color: var(--white);
  }
</style>
</head>
<body>
<main class="stage">
  <section class="card card-back">
    <div class="back-pattern" role="img" aria-label="Tiled repeat of the company emblem in tonal navy"></div>
    <div class="back-brand"><span class="brand-mark"></span><span>Verdant Pathworks</span></div>
  </section>

  <section class="card card-front">
    <div class="front-brand">
      <span class="brand-mark"></span>
      <span class="brand-name">Verdant Pathworks</span>
    </div>
    <div class="person">
      <div class="person-name">Dominic Ashvale</div>
      <div class="person-title">Owner</div>
    </div>
    <div class="divider"></div>
    <ul class="contact">
      <li>
        <svg viewBox="0 0 24 24" aria-hidden="true"><path d="M6.6 10.8c1.4 2.8 3.8 5.1 6.6 6.6l2.2-2.2c.3-.3.7-.4 1-.2 1.1.4 2.3.6 3.6.6.6 0 1 .4 1 1V20c0 .6-.4 1-1 1C10.6 21 3 13.4 3 4c0-.6.4-1 1-1h3.5c.6 0 1 .4 1 1 0 1.3.2 2.5.6 3.6.1.3 0 .7-.2 1z"/></svg>
        <span>555-017-3846</span>
      </li>
      <li>
        <svg viewBox="0 0 24 24" aria-hidden="true"><path d="M2 5h20v14H2z M2 5l10 8 10-8" fill="none" stroke="#1f3366" stroke-width="2"/></svg>
        <span>youremail@verdantmail.com</span>
      </li>
      <li>
        <svg viewBox="0 0 24 24" aria-hidden="true"><circle cx="12" cy="12" r="9" fill="none" stroke="#1f3366" stroke-width="2"/><path d="M3 12h18M12 3c3 3 3 15 0 18M12 3c-3 3-3 15 0 18" fill="none" stroke="#1f3366" stroke-width="1.6"/></svg>
        <span>www.yourwebsite.com</span>
      </li>
    </ul>
    <div class="address-band">Your address, city, state, ZIP 0000</div>
  </section>
</main>
</body>
</html>
```